Lanternfield Drinks business cards

We need a business card design for our new logo. The company is modern, progressive, professional, yet approachable. The key products are ready to drink bottles and cans of coffee based beverages.
These cards will be a critical part of the first impression made by our sales organization, business development team, and all external facing personnel.
Card can be a vertical or horizontal orientation.

Target Market(s)

Customers, suppliers, business partners

Industry/Entity Type

Business

Contact Information for Business Card

Business cards should feature Company Name and Logo.

Font styles to use
Serif

Colors

Designer to choose colors to be used in the design.

Requirements
Must have
• Strong readability of Name, phone #, mobile number and email address.
• Job title, website url, Street Address, and other details can be secondary level readability.
Nice to have
• High impact, simplistic quality design.
• Ok to utilize the 'H in the box' separate from the company name

```html
<!DOCTYPE html>
<html lang="en">
<head>
<meta charset="utf-8">
<title>Lanternfield Drinks business cards</title>
<link rel="stylesheet" href="https://fonts.googleapis.com/css2?family=Source+Serif+4:wght@400;700&display=swap">
<style>
  :root {
    --backdrop: #ece7e1;
    --card: #ffffff;
    --ink: #1d2340;
    --brand: #c94f2c;
    --brand-soft: #f6ddd0;
    --frame-line: #d8d8d8;
  }
  * { margin: 0; padding: 0; box-sizing: border-box; }
  html, body { width: 1200px; height: 1190px; overflow: hidden; }
  body {
    background: var(--backdrop);
    font-family: "Source Serif 4", serif;
    color: var(--ink);
    position: relative;
  }
  .card {
    position: absolute;
    left: 202px;
    width: 789px;
    background: var(--card);
    overflow: hidden;
    box-shadow: 0 10px 24px rgba(0,0,0,0.18);
  }
  .card--front { top: 137px; height: 457px; }
  .card--back { top: 653px; height: 442px; }

  .brand-mark {
    position: absolute;
    left: 73px;
    top: 61px;
    display: flex;
    align-items: center;
    gap: 12px;
  }
  .brand-mark__square {
    width: 66px; height: 66px;
    border: 4px solid var(--brand);
  }
  .brand-mark__name {
    font-weight: 700;
    font-size: 22px;
    color: var(--brand);
    line-height: 1;
    white-space: nowrap;
  }

  .contact {
    position: absolute;
    right: 447px;
    text-align: right;
    line-height: 1.2;
    white-space: nowrap;
  }
  .contact__icon {
    position: absolute;
    left: 358px;
    width: 38px;
  }
  .person-name { top: 163px; font-size: 27px; }
  .person-title { top: 197px; font-size: 13px; }
  .phones { top: 229px; font-size: 20px; line-height: 24px; }
  .email { top: 289px; font-size: 19px; }
  .website { top: 318px; font-size: 13px; }
  .address { top: 360px; font-size: 19px; }

  .faint-square {
    position: absolute;
    left: 454px; top: 113px;
    width: 420px; height: 420px;
    background: var(--brand-soft);
    opacity: 0.8;
  }
  .faint-square::after {
    content: "";
    position: absolute;
    left: 28px; top: 28px; right: 28px; bottom: 28px;
    background: var(--card);
    border: 3px solid var(--frame-line);
  }

  .back-brand {
    position: absolute;
    inset: 0;
    display: flex;
    flex-direction: column;
    align-items: center;
    justify-content: center;
    gap: 26px;
  }
  .back-brand__square {
    width: 190px; height: 190px;
    border: 14px solid var(--brand);
  }
  .back-brand__name {
    font-weight: 700;
    font-size: 54px;
    color: var(--brand);
    line-height: 1;
    white-space: nowrap;
  }
</style>
</head>
<body>
  <section class="card card--front">
    <div class="faint-square" aria-hidden="true"></div>

    <div class="brand-mark">
      <div class="brand-mark__square"></div>
      <div class="brand-mark__name">Lanternfield Drinks Co</div>
    </div>

    <p class="contact person-name">Marcus Ellery</p>
    <p class="contact person-title">-CEO</p>
    <svg class="contact__icon" style="top:168px" viewBox="0 0 40 48" aria-hidden="true">
      <circle cx="20" cy="12" r="10" fill="var(--ink)"/>
      <path d="M2 48 V36 Q2 26 12 25 L20 34 L28 25 Q38 26 38 36 V48 Z" fill="var(--ink)"/>
    </svg>

    <p class="contact phones">+44 7700 900145<br>(800) 555-0142</p>
    <svg class="contact__icon" style="top:229px" viewBox="0 0 40 48" aria-hidden="true">
      <rect x="9" y="4" width="22" height="40" rx="4" fill="var(--ink)"/>
      <rect x="13" y="10" width="14" height="20" fill="#fff"/>
      <rect x="13" y="34" width="14" height="4" fill="#fff"/>
    </svg>

    <p class="contact email">marcusellery@lanternfield.com</p>
    <p class="contact website">www.lanternfielddrinks.com</p>
    <svg class="contact__icon" style="top:288px" viewBox="0 0 40 40" aria-hidden="true">
      <text x="20" y="32" text-anchor="middle" font-family="Source Serif 4, serif" font-weight="700" font-size="40" fill="var(--ink)">@</text>
    </svg>

    <p class="contact address">214 Foundry Lane, Millbrook</p>
    <svg class="contact__icon" style="top:352px" viewBox="0 0 40 48" aria-hidden="true">
      <path d="M20 46 Q4 26 4 18 A16 16 0 0 1 36 18 Q36 26 20 46 Z" fill="var(--ink)"/>
      <circle cx="20" cy="18" r="6" fill="#fff"/>
    </svg>
  </section>

  <section class="card card--back">
    <div class="back-brand">
      <div class="back-brand__square"></div>
      <div class="back-brand__name">Lanternfield Drinks Co</div>
    </div>
  </section>
</body>
</html>
```